Brand new leaflet design creative ideas.

I need a flyer designed for my business

I run a pay weekly carpet business and need designs for a flyer this design i will also want to enable it on letterheads business cards and a logo from it when created.

my domain name is www.pallowmere.co.uk / www.pallowmere.com

Our main competitor i have attached his design to this brief to give you a bit of an idea on how we work, however i do not want a copycat design i want a brand new design something not like theres but eye catching direct to the point.

We are open to colour suggestions as long as the colours work.
Thank you.

Target Market(s)

This print material will be delivered to customers houses.

Industry/Entity Type

Flooring

Font styles to use
Serif
Sans Serif

Requirements
Must have
• Website domain name,
• Various print options CMYK, PDF
Nice to have
• Creativity eye catching
Should not have
• SHOULD NOT BE A COPYCAT DESIGN SOMETHING NEW & CREATIVE

```html
<!DOCTYPE html>
<html lang="en">
<head>
<meta charset="utf-8">
<title>Pallowmere – Pay Weekly Carpets and Vinyls</title>
<link rel="stylesheet" href="https://fonts.googleapis.com/css2?family=Barlow+Condensed:wght@500;600;700&family=Playfair+Display:ital,wght@0,900;1,700&display=swap">
<style>
  :root {
    --cream: #f6efe3;
    --navy: #14213d;
    --navy-deep: #0d1629;
    --coral: #e4572e;
    --gold: #f2b134;
    --sand: #d9c2a0;
    --sand-dark: #a9865c;
    --white: #ffffff;
  }
  * { box-sizing: border-box; margin: 0; padding: 0; }
  html, body { width: 864px; height: 1200px; overflow: hidden; background: var(--cream); }
  .flyer { position: relative; width: 864px; height: 1200px; overflow: hidden; background: var(--cream); }

  .brand {
    position: absolute; left: 56px; top: 48px;
    display: flex; align-items: center; gap: 12px;
    font-family: "Barlow Condensed", sans-serif; font-weight: 700;
    font-size: 32px; letter-spacing: 2px; text-transform: uppercase; color: var(--navy);
  }
  .brand-square { width: 22px; height: 22px; background: var(--coral); }

  .headline { position: absolute; left: 56px; top: 112px; width: 752px; color: var(--navy); }
  .headline .lead {
    display: block; font-family: "Playfair Display", serif; font-weight: 900;
    font-size: 108px; line-height: 1.02;
  }
  .headline .rest {
    display: block; font-family: "Playfair Display", serif; font-style: italic; font-weight: 700;
    font-size: 66px; line-height: 1.1; color: var(--coral);
  }

  .room-photo {
    position: absolute; left: 56px; top: 372px; width: 752px; height: 330px;
    border-radius: 24px;
    background:
      radial-gradient(ellipse at 30% 35%, rgba(255,255,255,0.55) 0%, rgba(255,255,255,0) 55%),
      linear-gradient(180deg, #e9ddcb 0%, #dcc7a6 55%, var(--sand) 70%, var(--sand-dark) 100%);
  }

  .offer-badge {
    position: absolute; left: 626px; top: 300px; width: 200px; height: 200px;
    border-radius: 50%; background: var(--coral);
    box-shadow: 0 0 0 8px var(--cream);
    display: flex; flex-direction: column; align-items: center; justify-content: center;
    font-family: "Barlow Condensed", sans-serif; font-weight: 700; text-transform: uppercase;
    color: var(--white); text-align: center; line-height: 1;
  }
  .offer-badge .small { font-size: 26px; letter-spacing: 1px; }
  .offer-badge .big { font-size: 40px; margin: 4px 0; }

  .benefits {
    position: absolute; left: 56px; top: 736px; width: 752px;
    display: grid; grid-template-columns: repeat(3, 1fr);
    list-style: none; text-align: center;
  }
  .benefit {
    display: flex; flex-direction: column; align-items: center; gap: 12px;
    font-family: "Barlow Condensed", sans-serif; font-weight: 600; font-size: 34px;
    text-transform: uppercase; letter-spacing: 1px; color: var(--navy);
  }
  .benefit + .benefit { border-left: 2px solid var(--sand); }
  .tick { width: 52px; height: 52px; }

  .contact {
    position: absolute; left: 0; top: 910px; width: 864px; height: 290px;
    background: var(--navy);
    display: flex; flex-direction: column; align-items: center; justify-content: center;
    font-family: "Barlow Condensed", sans-serif; color: var(--white); text-align: center;
  }
  .contact::before {
    content: ""; position: absolute; left: 0; top: 0; width: 864px; height: 10px; background: var(--gold);
  }
  .contact .call { font-weight: 600; font-size: 28px; letter-spacing: 4px; text-transform: uppercase; color: var(--gold); }
  .contact .phone {
    display: flex; align-items: center; gap: 16px;
    font-weight: 700; font-size: 72px; line-height: 1.15; letter-spacing: 1px;
  }
  .phone-icon { width: 50px; height: 50px; }
  .contact .web { font-weight: 500; font-size: 34px; letter-spacing: 1px; }
  .contact .web strong { font-weight: 700; color: var(--gold); }
</style>
</head>
<body>
<main class="flyer">
  <div class="brand"><span class="brand-square"></span>Pallowmere</div>

  <h1 class="headline">
    <span class="lead">Pay weekly</span>
    <span class="rest">carpets and vinyls</span>
  </h1>

  <div class="room-photo" role="img" aria-label="Living room with a freshly fitted soft carpet and a sofa"></div>

  <div class="offer-badge">
    <span class="small">Amazing</span>
    <span class="big">Carpet</span>
    <span class="small">Offers!</span>
  </div>

  <ul class="benefits">
    <li class="benefit">
      <svg class="tick" viewBox="0 0 52 52" aria-hidden="true"><circle cx="26" cy="26" r="26" fill="#e4572e"/><path d="M15 27l7 7 15-16" fill="none" stroke="#fff" stroke-width="5" stroke-linecap="round" stroke-linejoin="round"/></svg>
      Pay weekly
    </li>
    <li class="benefit">
      <svg class="tick" viewBox="0 0 52 52" aria-hidden="true"><circle cx="26" cy="26" r="26" fill="#e4572e"/><path d="M15 27l7 7 15-16" fill="none" stroke="#fff" stroke-width="5" stroke-linecap="round" stroke-linejoin="round"/></svg>
      Interest free
    </li>
    <li class="benefit">
      <svg class="tick" viewBox="0 0 52 52" aria-hidden="true"><circle cx="26" cy="26" r="26" fill="#e4572e"/><path d="M15 27l7 7 15-16" fill="none" stroke="#fff" stroke-width="5" stroke-linecap="round" stroke-linejoin="round"/></svg>
      No credit checks
    </li>
  </ul>

  <footer class="contact">
    <p class="call">To apply please call</p>
    <p class="phone">
      <svg class="phone-icon" viewBox="0 0 24 24" aria-hidden="true"><path fill="#f2b134" d="M6.6 10.8a15.1 15.1 0 0 0 6.6 6.6l2.2-2.2c.3-.3.7-.4 1-.2 1.1.4 2.3.6 3.6.6.6 0 1 .4 1 1V20c0 .6-.4 1-1 1A17 17 0 0 1 3 4c0-.6.4-1 1-1h3.5c.6 0 1 .4 1 1 0 1.3.2 2.5.6 3.6.1.3 0 .7-.2 1z"/></svg>
      0207 555 0142
    </p>
    <p class="web">or visit <strong>www.pallowmere.co.uk</strong></p>
  </footer>
</main>
</body>
</html>
```